The name of my company is Tolmen Refacing LLC and I would like the sub text to say "Cabinet Refacing and Countertops". Have my name Dorian Tolmen, Owner / Sales, contact info: Cell: 360-555-0147 / Email: dorian.tolmen@quenmail.com

Simple, Clean, and Organized. With colors that will appeal to the eye.

Target Market(s)

Houses and Apartments

Industry/Entity Type

Cabinet Refacing

Contact Information for Business Card

Company name and sub text Dorian Tolmen - Owner / Sales, my cell phone number and email

Requirements
Must have
• Business name, my name / position, and my contact info
Nice to have
• Simple. Organized. Appealing to the eye

```html
<!DOCTYPE html>
<html lang="en">
<head>
<meta charset="utf-8">
<title>Tolmen Refacing LLC — Business Card</title>
<link rel="stylesheet" href="https://fonts.googleapis.com/css2?family=Montserrat:wght@300;500;600;800&family=Barlow+Semi+Condensed:wght@600&display=swap">
<style>
  :root {
    --paper: #f4f1ea;
    --gold: #f9c35c;
    --teal: #163742;
  }
  * { box-sizing: border-box; margin: 0; padding: 0; }
  html, body { width: 1200px; height: 1200px; overflow: hidden; }
  body { background: var(--paper); position: relative; font-family: "Montserrat", sans-serif; }

  .card { position: absolute; width: 734px; height: 420px; left: 233px; overflow: hidden; }
  .card--front { top: 148px; background: var(--gold); color: var(--teal); }
  .card--back { top: 632px; background: var(--teal); color: var(--gold); }

  .divider { position: absolute; left: 335px; width: 7px; background: var(--teal); }
  .divider--top { top: 0; height: 118px; }
  .divider--mid { top: 141px; height: 137px; }
  .divider--bottom { top: 302px; height: 118px; }

  .brand { position: absolute; text-align: center; }
  .brand__mark { display: block; margin: 0 auto; border-radius: 50%; }
  .brand__name { font-weight: 300; letter-spacing: 0.5px; white-space: nowrap; }
  .brand__tagline { font-family: "Barlow Semi Condensed", sans-serif; font-weight: 600; white-space: nowrap; }

  .card--front .brand { left: 0; width: 335px; top: 140px; }
  .card--front .brand__mark { width: 56px; height: 56px; background: var(--teal); margin-bottom: 14px; }
  .card--front .brand__name { font-size: 23px; line-height: 1; }
  .card--front .brand__tagline { font-size: 12px; margin-top: 8px; letter-spacing: 0.3px; }

  .contact { position: absolute; left: 386px; top: 112px; width: 320px; }
  .contact__company { font-weight: 800; font-size: 22px; letter-spacing: 0.6px; text-transform: uppercase; line-height: 1; white-space: nowrap; }
  .contact__tagline { font-weight: 600; font-size: 9px; letter-spacing: 2px; text-transform: uppercase; margin-top: 7px; white-space: nowrap; }
  .contact__person { margin-top: 20px; font-weight: 600; font-size: 16px; line-height: 1.2; white-space: nowrap; }
  .contact__role { font-weight: 500; font-size: 12px; letter-spacing: 1px; text-transform: uppercase; margin-top: 3px; white-space: nowrap; }
  .contact__line { display: flex; align-items: center; gap: 10px; font-weight: 600; font-size: 16px; white-space: nowrap; }
  .contact__line--phone { margin-top: 18px; }
  .contact__line--email { margin-top: 14px; }
  .contact__icon { width: 21px; height: 21px; flex: none; }

  .card--back .brand { left: 0; width: 734px; top: 100px; }
  .card--back .brand__mark { width: 92px; height: 92px; background: var(--gold); margin-bottom: 22px; }
  .card--back .brand__name { font-size: 44px; line-height: 1; }
  .card--back .brand__tagline { font-size: 19px; margin-top: 12px; letter-spacing: 0.4px; }

  .rule-set { position: absolute; left: 138px; top: 387px; display: flex; gap: 22px; }
  .rule-set__bar { width: 138px; height: 7px; background: var(--gold); }
</style>
</head>
<body>

  <section class="card card--front" aria-label="Business card front">
    <div class="divider divider--top"></div>
    <div class="divider divider--mid"></div>
    <div class="divider divider--bottom"></div>

    <div class="brand">
      <span class="brand__mark"></span>
      <div class="brand__name">TOLMEN REFACING LLC</div>
      <div class="brand__tagline">CABINET REFACING AND COUNTERTOPS</div>
    </div>

    <div class="contact">
      <div class="contact__company">Tolmen Refacing LLC</div>
      <div class="contact__tagline">Cabinet Refacing and Countertops</div>
      <div class="contact__person">Dorian Tolmen</div>
      <div class="contact__role">Owner / Sales</div>
      <div class="contact__line contact__line--phone">
        <svg class="contact__icon" viewBox="0 0 24 24" fill="none" stroke="currentColor" stroke-width="1.6" stroke-linecap="round" stroke-linejoin="round">
          <path d="M5 3.5l3 0.2 1.6 4-2 1.6a12 12 0 0 0 6.8 6.8l1.6-2 4 1.6 0.2 3a2 2 0 0 1-2.2 2A17 17 0 0 1 3 5.7 2 2 0 0 1 5 3.5z"/>
          <path d="M14.5 3.5a7 7 0 0 1 6 6"/>
          <path d="M14 7a3.5 3.5 0 0 1 3 3"/>
        </svg>
        <span>360-555-0147</span>
      </div>
      <div class="contact__line contact__line--email">
        <svg class="contact__icon" viewBox="0 0 24 24" fill="none" stroke="currentColor" stroke-width="1.6" stroke-linejoin="round">
          <rect x="2" y="5" width="20" height="14"/>
          <path d="M2 5l10 8 10-8M2 19l7.5-7.5M22 19l-7.5-7.5"/>
        </svg>
        <span>dorian.tolmen@quenmail.com</span>
      </div>
    </div>
  </section>

  <section class="card card--back" aria-label="Business card back">
    <div class="brand">
      <span class="brand__mark"></span>
      <div class="brand__name">TOLMEN REFACING LLC</div>
      <div class="brand__tagline">CABINET REFACING AND COUNTERTOPS</div>
    </div>
    <div class="rule-set">
      <span class="rule-set__bar"></span>
      <span class="rule-set__bar"></span>
      <span class="rule-set__bar"></span>
    </div>
  </section>

</body>
</html>
```